Atelier Marrow Architecture business card

We need to update our business card. We do high end custom residential, hospitality, and wellness architecture. We focus on creating unique spaces and design around the five senses, believing that architecture's true impact is not on our surroundings, but within us. We would like to see designs are instill a sense of calm awe. They should be crisp, fresh, clean, authentic, & contemporary without being sterile, overworked, or harsh. White space is important. Alternative materials are an option if natural. We have created our own logo and would like designs to incorporate it. However, we are willing to see alternatives if the logo becomes a stumbling block and you have an alternate you suggest. Card must have the following information:
Atelier Marrow Architecture, Inc.
728 Holloway Ct. NE Atlanta, GA 30318
Marcus T. Whitcombe, AIA, NCARB, LEED AP BD+C
ateliermarrow.example

Target Market(s)

Higher net worth individuals with an appreciation for design, nature, sustainability,

Industry/Entity Type

Architect

Contact Information for Business Card

See above. The title of Owner or Architect is helpful but not necessary. Minimalism should trump additional information.

Font styles to use
Serif
Sans Serif

Requirements
Must have
• It should look professional. It must use logo
Should not have
• caligraphy, animals, anything that is cute,

```html
<!DOCTYPE html>
<html lang="en">
<head>
<meta charset="utf-8">
<title>Atelier Marrow Architecture — Business Card</title>
<link rel="stylesheet" href="https://fonts.googleapis.com/css2?family=Josefin+Sans:wght@300&family=Libre+Baskerville:wght@400;700&display=swap">
<style>
  :root {
    --page: #ecebe8;
    --navy-deep: #15172a;
    --navy: #23263c;
    --navy-light: #2c3049;
    --ink-light: #f3f3f5;
    --ink-muted: #c9cbd6;
    --band: #d6d6d8;
    --band-ink: #8e8e92;
    --icon: #9a9a9e;
  }
  * { box-sizing: border-box; margin: 0; padding: 0; }
  html, body { width: 1200px; height: 1200px; overflow: hidden; }
  body {
    background: var(--page);
    display: flex;
    flex-direction: column;
    align-items: center;
    justify-content: center;
    gap: 80px;
  }
  .card {
    position: relative;
    width: 700px;
    height: 400px;
    overflow: hidden;
    box-shadow: 0 10px 30px rgba(20, 22, 40, 0.18);
  }
  .card-surface {
    position: absolute;
    inset: 0;
    background: radial-gradient(ellipse at 45% 45%, var(--navy-light) 0%, var(--navy) 45%, var(--navy-deep) 100%);
  }

  /* Front */
  .wordmark {
    position: absolute;
    left: 0; right: 0; top: 50%;
    transform: translateY(-50%);
    text-align: center;
    font-family: "Josefin Sans", sans-serif;
    font-weight: 300;
    color: var(--ink-light);
    font-size: 30px;
    letter-spacing: 0.32em;
    text-transform: uppercase;
  }

  /* Back */
  .identity {
    position: absolute;
    top: 118px;
    left: 0; right: 0;
    text-align: center;
    padding-left: 70px;
  }
  .identity-name {
    font-family: "Libre Baskerville", serif;
    font-weight: 700;
    font-size: 28px;
    letter-spacing: 0.04em;
    color: var(--ink-light);
    text-transform: uppercase;
  }
  .identity-credentials {
    margin-top: 22px;
    font-family: "Libre Baskerville", serif;
    font-size: 12px;
    letter-spacing: 0.04em;
    color: var(--ink-muted);
    text-transform: uppercase;
  }
  .contact-band {
    position: absolute;
    left: 0; right: 0; bottom: 0;
    height: 140px;
    background: var(--band);
    display: grid;
    grid-template-columns: 1fr 1fr;
    align-content: center;
    row-gap: 22px;
    padding: 0 40px 0 60px;
  }
  .contact-item {
    display: flex;
    align-items: center;
    gap: 18px;
    font-family: "Libre Baskerville", serif;
    font-size: 11px;
    letter-spacing: 0.03em;
    color: var(--band-ink);
    text-transform: uppercase;
  }
  .contact-item svg { width: 26px; height: 26px; flex: none; fill: var(--icon); }
  .contact-phone { grid-column: 1; grid-row: 1; }
  .contact-address { grid-column: 1; grid-row: 2; }
  .contact-email { grid-column: 2; grid-row: 1; }
  .contact-web { grid-column: 2; grid-row: 2; }
</style>
</head>
<body>

  <section class="card card-front">
    <div class="card-surface" role="img" aria-label="Dark navy surface with a subtle square grid pattern"></div>
    <p class="wordmark">Atelier Marrow Architecture</p>
  </section>

  <section class="card card-back">
    <div class="card-surface" role="img" aria-label="Dark navy surface with a subtle square grid pattern"></div>
    <div class="identity">
      <h1 class="identity-name">Marcus T. Whitcombe</h1>
      <p class="identity-credentials">AIA, NCARB, LEED AP BD+C</p>
    </div>
    <div class="contact-band">
      <p class="contact-item contact-phone">
        <svg viewBox="0 0 24 24" aria-hidden="true"><path d="M7 2c1 0 1.6.6 1.9 1.5l.9 3c.2.8 0 1.5-.6 2l-1.4 1.1c.9 2.4 2.4 4.3 4.4 5.8l1.4-1c.6-.5 1.4-.6 2.1-.3l2.8 1.2c.9.4 1.3 1.1 1.2 2l-.4 2.4c-.2 1-1 1.6-2 1.6C9.6 21.3 3.4 13 4.8 4.1 5 2.9 5.8 2 7 2z"/></svg>
        0800-your-number-here
      </p>
      <p class="contact-item contact-address">
        <svg viewBox="0 0 24 24" aria-hidden="true"><path d="M12 3 2 12h3v9h5v-6h4v6h5v-9h3z"/></svg>
        728 Holloway Ct. NE Atlanta, GA 30318
      </p>
      <p class="contact-item contact-email">
        <svg viewBox="0 0 24 24" aria-hidden="true"><path d="M2 5h20v2l-10 6L2 7zm0 4 10 6 10-6v10H2z"/></svg>
        youremail@here.com
      </p>
      <p class="contact-item contact-web">
        <svg viewBox="0 0 24 24" aria-hidden="true"><path d="M12 2a10 10 0 1 0 0 20 10 10 0 0 0 0-20zm0 1.6c.9 0 2.2 1.8 2.7 5.4H9.3C9.8 5.4 11.1 3.6 12 3.6zM8.2 4.4C7.8 5.6 7.5 7.2 7.4 9H4.1a8.4 8.4 0 0 1 4.1-4.6zm7.6 0A8.4 8.4 0 0 1 19.9 9h-3.3c-.1-1.8-.4-3.4-.8-4.6zM3.7 10.6h3.6v2.8H3.7a8.3 8.3 0 0 1 0-2.8zm5.3 0h6v2.8H9zm7.7 0h3.6a8.3 8.3 0 0 1 0 2.8h-3.6zM4.1 15h3.3c.1 1.8.4 3.4.8 4.6A8.4 8.4 0 0 1 4.1 15zm5.2 0h5.4c-.5 3.6-1.8 5.4-2.7 5.4s-2.2-1.8-2.7-5.4zm7.3 0h3.3a8.4 8.4 0 0 1-4.1 4.6c.4-1.2.7-2.8.8-4.6z"/></svg>
        www.ateliermarrow.example
      </p>
    </div>
  </section>

</body>
</html>
```